I need a book cover designed for my book entitled Turn Up ~ The Weekly Swatch Project --- This book

I need a book cover designed for this book. I envision the book size being 6x6. This book will take the reader, week by week, over the course of a year, into my journey of going bold through the weekly changing of my nail polish color. The book will contain pictures of the nail polish colors as well as weekly journal entries, monthly summaries and then an overall conlusion that detail the personal discovery and growth that took place through this simple, yet consistent practice of going bold by changing my nail polish.

Reason: I would like to extend the deadline by five days because I have several people looking at the designs and providing their thoughts and a few people have been unable to do so this week! Thank you SO much! Cleo :)

```html
<!DOCTYPE html>
<html lang="en">
<head>
<meta charset="utf-8">
<title>Turn Up! The Weekly Swatch Project – Book Cover</title>
<link rel="stylesheet" href="https://fonts.googleapis.com/css2?family=Roboto+Slab:wght@700&family=Raleway:wght@300;400&display=swap">
<style>
  :root {
    --paper: #efeeea;
    --magenta: #d63aa6;
    --magenta-deep: #b81f86;
    --ink: #2f2f31;
    --polish-yellow: #f2c514;
    --polish-red: #e0124f;
    --polish-green: #8cc63a;
  }
  html, body {
    margin: 0;
    padding: 0;
    width: 1200px;
    height: 1200px;
    overflow: hidden;
    background: var(--paper);
  }
  .cover {
    position: relative;
    width: 1200px;
    height: 1200px;
    background: linear-gradient(180deg, #f3f2ef 0%, var(--paper) 60%, #f6f5f3 100%);
    overflow: hidden;
  }
  .polish-top {
    position: absolute;
    left: 720px;
    top: -120px;
    width: 290px;
    height: 290px;
    border-radius: 50%;
    background: radial-gradient(circle at 45% 60%, var(--magenta-deep) 0 18%, var(--magenta) 30%, #e58ac8 62%, #f1d6e8 80%, rgba(255,255,255,0) 82%);
  }
  .drip {
    position: absolute;
    left: 0;
    top: 0;
  }
  .title-block {
    position: absolute;
    left: 250px;
    top: 370px;
    width: 720px;
  }
  .title {
    margin: 0;
    font-family: "Roboto Slab", serif;
    font-weight: 700;
    font-size: 112px;
    line-height: 1;
    color: var(--magenta);
    letter-spacing: -1px;
  }
  .title-rule {
    height: 3px;
    width: 600px;
    background: var(--magenta);
    margin: 10px 0 12px;
  }
  .subtitle {
    margin: 0;
    font-family: "Raleway", sans-serif;
    color: var(--ink);
    line-height: 1.02;
  }
  .subtitle-line1 {
    display: block;
    font-weight: 300;
    font-size: 76px;
    padding-left: 8px;
  }
  .subtitle-line2 {
    display: block;
    font-weight: 400;
    font-size: 104px;
    padding-left: 20px;
  }
  .polish-bottles {
    position: absolute;
    left: 0;
    top: 800px;
    width: 1080px;
    height: 290px;
    background:
      radial-gradient(ellipse 22% 45% at 20% 55%, var(--polish-yellow) 0 60%, rgba(242,197,20,0) 100%),
      radial-gradient(ellipse 14% 40% at 44% 40%, var(--polish-red) 0 55%, rgba(224,18,79,0) 100%),
      radial-gradient(ellipse 22% 38% at 76% 48%, var(--polish-green) 0 55%, rgba(140,198,58,0) 100%),
      linear-gradient(180deg, rgba(255,255,255,0) 0%, rgba(255,255,255,0.6) 100%);
  }
</style>
</head>
<body>
  <main class="cover">
    <div class="polish-top" role="img" aria-label="Photo: open bottle of magenta nail polish seen from above"></div>

    <svg class="drip" width="1200" height="1200" aria-hidden="true">
      <path d="M865 120 C868 250 872 380 876 500" stroke="var(--magenta)" stroke-width="5" fill="none" stroke-linecap="round"/>
      <ellipse cx="876" cy="505" rx="10" ry="16" fill="var(--magenta)"/>
    </svg>

    <section class="title-block">
      <h1 class="title">Turn Up!</h1>
      <div class="title-rule"></div>
      <p class="subtitle">
        <span class="subtitle-line1">The Weekly Swatch</span>
        <span class="subtitle-line2">Project</span>
      </p>
    </section>

    <div class="polish-bottles" role="img" aria-label="Photo: three tipped-over nail polish bottles in yellow, red and green spilling polish"></div>
  </main>
</body>
</html>
```